FLOUR BAG DESIGN

• Bag dimensions: H=280 mm, A=105 mm, B=65 mm (look at the picture »dimensions«)
• Bag will be used for different types of flour (wheat flour, corn flour, buckwheat flour, etc.) and porridge (buckwheat, millet, etc. ) so we are looking for universal design that will suit to all of them. Please have in mind that somewhere on the front side (AxH) there needs to be some space for the name of the flour/porridge.
• I also uploaded design of an existing bag just in case you want to see it. Design on the bag represents the mill where our business started. We could say that existing bag is very traditional, we are looking for a little bit more modern style bag but still want to emphasize the link to our tradition.

I forgot to select "10 days " when desribing the label desing I need, before posting the project

• • We would like to integrate our logo (look at the picture »logo«) and text which is also present on the current bag. Front side AxH: Brezarjev Mlin (name of the company), Fužina – Zagradec (name of the village), Meljemo že od 1682 (meaning Flour milling since 1682). On the right side: same as on the picture »current bag (dimensions BxH)«.

```html
<!DOCTYPE html>
<html lang="sl">
<head>
<meta charset="utf-8">
<title>Brezarjev Mlin – bočna stran vrečke</title>
<link href="https://fonts.googleapis.com/css2?family=Signika:wght@300;400;600&display=swap" rel="stylesheet">
<style>
  :root {
    --paper: #ffffff;
    --flour-gold: #fcd385;
    --mill-brown: #7a4208;
    --accent-orange: #f5a623;
    --crop-black: #1a1a1a;
  }
  html, body {
    margin: 0;
    width: 1200px;
    height: 1200px;
    overflow: hidden;
    background: var(--paper);
  }
  .canvas {
    position: relative;
    width: 1200px;
    height: 1200px;
  }
  .side-panel {
    position: absolute;
    left: 468px;
    top: 0;
    width: 264px;
    height: 1200px;
    background: var(--flour-gold);
    font-family: "Signika", "Trebuchet MS", sans-serif;
    color: var(--mill-brown);
  }
  .crop-marks {
    position: absolute;
    left: 0;
    top: 0;
  }
  .origin-seal {
    position: absolute;
    left: 58px;
    top: 706px;
    display: flex;
    flex-direction: column;
    align-items: flex-start;
    gap: 16px;
  }
  .origin-seal .seal-dot {
    width: 60px;
    height: 60px;
    border-radius: 50%;
    background: var(--mill-brown);
    margin-left: 0;
  }
  .origin-seal .seal-name {
    font-size: 11px;
    font-weight: 400;
    letter-spacing: 2px;
    text-transform: uppercase;
    margin-left: 1px;
  }
  .rule {
    position: absolute;
    left: 0;
    width: 264px;
    height: 2px;
    background: var(--accent-orange);
  }
  .rule.upper { top: 805px; }
  .rule.lower { top: 849px; }
  .brand-band {
    position: absolute;
    left: 0;
    top: 810px;
    width: 264px;
    height: 38px;
    background: linear-gradient(180deg, #84490c 0%, var(--mill-brown) 50%, #6e3a06 100%);
  }
  .contact {
    position: absolute;
    left: 0;
    top: 852px;
    width: 264px;
    text-align: center;
    line-height: 22.5px;
    font-size: 17px;
    font-weight: 300;
  }
  .contact .company {
    font-weight: 600;
    font-size: 17px;
    text-transform: uppercase;
  }
  .contact .owner {
    font-weight: 600;
    font-size: 16px;
  }
  .contact p { margin: 0; }
  .website {
    position: absolute;
    left: 0;
    top: 1018px;
    width: 264px;
    text-align: center;
    font-size: 14px;
    font-weight: 600;
  }
</style>
</head>
<body>
<div class="canvas">
  <section class="side-panel">
    <svg class="crop-marks" width="264" height="1200" viewBox="0 0 264 1200" aria-hidden="true">
      <g stroke="var(--crop-black)" stroke-width="1.5">
        <line x1="30" y1="0" x2="30" y2="20"/>
        <line x1="234" y1="0" x2="234" y2="20"/>
        <line x1="0" y1="30" x2="21" y2="30"/>
        <line x1="243" y1="30" x2="264" y2="30"/>
        <line x1="0" y1="1170" x2="21" y2="1170"/>
        <line x1="243" y1="1170" x2="264" y2="1170"/>
        <line x1="30" y1="1180" x2="30" y2="1200"/>
        <line x1="234" y1="1180" x2="234" y2="1200"/>
      </g>
    </svg>

    <div class="origin-seal">
      <div class="seal-dot"></div>
      <span class="seal-name">Domača izbira</span>
    </div>

    <div class="rule upper"></div>
    <div class="brand-band"></div>
    <div class="rule lower"></div>

    <div class="contact">
      <p class="company">Brezarjev Mlin</p>
      <p class="owner">Tomaž Kranjc s.p.</p>
      <p>Lipovec 12</p>
      <p>1310 Ribnica</p>
      <p>T: 01 555 20 20</p>
      <p>M: 040 555 318</p>
    </div>

    <div class="website">www.brezarjev-mlin.si</div>
  </section>
</div>
</body>
</html>
```